Husband and i just started a new Hotshot trucking company, Its a pick up and delivery service. We own our own 40 foot gooseneck trailer... Called Roadbird Hauling LLC. We are needing some business cards made to help advertise our new company. We are based out of Ft Worth Tx. We are the ones who transports what ever loads to where ever they need to go, at any time. We stride for success. And we wont take no for an answer.
What we need on there is the following: need it to be all caps please.

DOUGLAS PRATHER "BO"
555-318-4426
ROADBIRDHAULINGLLC@MAILNEST.EXAMPLE

SHELBY CORWIN
555-604-7153

We have a couple logos already made. however we are always game to see new ideas. Thank you for your time.

Target Market(s)

Youth, middle aged. Home buyers

Industry/Entity Type

Hotshot Trucking Pick up and Delivery Service

Contact Information for Business Card

DOUGLAS PRATHER "BO" 555-318-4426 ROADBIRDHAULINGLLC@MAILNEST.EXAMPLE SHELBY CORWIN 555-604-7153 ROADBIRDHAULINGLLC@MAILNEST.EXAMPLE

Font styles to use
Serif
Script

Colors
0054AA
0677BA
7BADD7
CADEEF
E8F1F8
0094D4
00A9DD
6FCCEA
C7EBF8
E9F6FB

Requirements
Must have
• Our company logo. and look one of a kind. also has to be able to catch some ones eye and stand out
Nice to have
• open for ideas..

```html
<!DOCTYPE html>
<html lang="en">
<head>
<meta charset="utf-8">
<title>Roadbird Hauling LLC — Business Cards</title>
<link href="https://fonts.googleapis.com/css2?family=Roboto+Condensed:wght@400;700&display=swap" rel="stylesheet">
<style>
  :root {
    --page: #d9d9d9;
    --navy-deep: #14224f;
    --navy: #0f2f7a;
    --royal: #0a4aa8;
    --sky: #6fccea;
    --ice: #e9f6fb;
    --white: #ffffff;
    --shadow: rgba(0, 0, 0, 0.28);
  }
  * { margin: 0; padding: 0; box-sizing: border-box; }
  html, body {
    width: 1200px; height: 846px; overflow: hidden;
    background: var(--page);
    font-family: "Roboto Condensed", "Arial Narrow", sans-serif;
  }
  .sheet {
    position: relative; width: 1200px; height: 846px;
    display: flex; align-items: center; justify-content: center; gap: 50px;
  }
  .card {
    position: relative; width: 540px; height: 309px; overflow: hidden;
    background: linear-gradient(120deg, var(--navy-deep) 0%, var(--navy) 35%, var(--royal) 55%, var(--navy) 75%, var(--navy-deep) 100%);
    box-shadow: 0 14px 30px var(--shadow);
    color: var(--white);
  }
  .card__bands { position: absolute; inset: 0; width: 100%; height: 100%; }
  .brand {
    position: absolute; display: flex; align-items: center; gap: 10px;
    font-weight: 700; letter-spacing: 0.5px; color: var(--white);
    white-space: nowrap;
  }
  .brand__mark { flex: none; border-radius: 50%; background: var(--sky); }
  .card--front .brand { left: 44px; top: 62px; font-size: 28px; }
  .card--front .brand__mark { width: 24px; height: 24px; }
  .card--back .brand {
    left: 0; right: 0; top: 0; bottom: 0; justify-content: center;
    font-size: 40px;
  }
  .card--back .brand__mark { width: 34px; height: 34px; }
  .contact { position: absolute; text-transform: uppercase; line-height: 1.3; white-space: nowrap; }
  .contact__name { font-weight: 700; font-size: 18px; letter-spacing: 0.3px; }
  .contact__line { font-weight: 400; font-size: 13px; color: var(--ice); letter-spacing: 0.3px; }
  .contact--secondary { left: 272px; top: 132px; }
  .contact--primary { left: 60px; top: 206px; }
</style>
</head>
<body>
<main class="sheet">
  <section class="card card--front" aria-label="Business card front">
    <svg class="card__bands" viewBox="0 0 540 309" preserveAspectRatio="none" aria-hidden="true">
      <polygon points="120,0 200,0 200,309 120,309" fill="#ffffff" opacity="0.04"/>
      <polygon points="330,0 400,0 400,309 330,309" fill="#000000" opacity="0.08"/>
      <polygon points="0,180 540,150 540,190 0,220" fill="#0094d4" opacity="0.10"/>
    </svg>
    <div class="brand"><span class="brand__mark"></span>ROADBIRD HAULING LLC</div>
    <div class="contact contact--secondary">
      <p class="contact__name">SHELBY CORWIN</p>
      <p class="contact__line">CALL: 555-604-7153</p>
      <p class="contact__line">ROADBIRDHAULINGLLC@MAILNEST.EXAMPLE</p>
    </div>
    <div class="contact contact--primary">
      <p class="contact__name">DOUGLAS PRATHER "BO"</p>
      <p class="contact__line">CALL: 555-318-4426</p>
      <p class="contact__line">ROADBIRDHAULINGLLC@MAILNEST.EXAMPLE</p>
    </div>
  </section>

  <section class="card card--back" aria-label="Business card back">
    <svg class="card__bands" viewBox="0 0 540 309" preserveAspectRatio="none" aria-hidden="true">
      <polygon points="90,0 170,0 170,309 90,309" fill="#000000" opacity="0.08"/>
      <polygon points="380,0 450,0 450,309 380,309" fill="#ffffff" opacity="0.04"/>
      <polygon points="0,150 540,120 540,160 0,190" fill="#0094d4" opacity="0.10"/>
    </svg>
    <div class="brand"><span class="brand__mark"></span>ROADBIRD HAULING LLC</div>
  </section>
</main>
</body>
</html>
```